Brightwave Business Card

Professional Business Card Design required using the attached contact information.

Contact information can be rearranged as required.

The company is a new start up venture developing solar systems, the branding should be in keeping with that of one of the investors whose website is as follows https://www.quorvex.com/

```html
<!DOCTYPE html>
<html lang="en">
<head>
<meta charset="utf-8">
<title>Brightwave Renewables – Business Card</title>
<link rel="stylesheet" href="https://fonts.googleapis.com/css2?family=Roboto:wght@400;500;700&display=swap">
<style>
  :root {
    --backdrop: #3a3a3a;
    --card-black: #1c1c1c;
    --band-black: #202020;
    --brand-green: #2b6a53;
    --text-white: #ffffff;
    --text-soft: #e2e8e5;
    --wordmark-grey: #5a5a5a;
    --wordmark-light: #e6e6e6;
  }
  * { margin: 0; padding: 0; box-sizing: border-box; }
  html, body {
    width: 799px; height: 1200px; overflow: hidden;
    background: var(--backdrop);
    font-family: "Roboto", Arial, sans-serif;
  }
  .canvas {
    width: 799px; height: 1200px;
    display: flex; flex-direction: column;
    align-items: center; justify-content: space-around;
    padding: 60px 0;
  }
  .card {
    width: 600px; height: 343px;
    border-radius: 4px;
    overflow: hidden;
    box-shadow: 0 14px 30px rgba(0,0,0,0.45);
    position: relative;
  }
  /* Front */
  .card-front {
    background: var(--card-black);
    display: flex; align-items: center; justify-content: center;
  }
  .front-wordmark {
    font-weight: 500;
    font-size: 30px;
    letter-spacing: 8px;
    color: var(--wordmark-grey);
    text-transform: uppercase;
  }
  /* Back */
  .card-back { background: var(--brand-green); }
  .back-band {
    height: 104px;
    background: var(--band-black);
    display: flex; align-items: center;
    padding-left: 40px;
  }
  .back-wordmark {
    font-weight: 500;
    font-size: 31px;
    letter-spacing: 3px;
    color: var(--wordmark-light);
    text-transform: uppercase;
  }
  .back-body { padding: 10px 40px 0; }
  .person-name {
    font-weight: 700; font-size: 22px;
    color: var(--text-white);
  }
  .person-role {
    font-size: 12px; color: var(--text-soft);
    margin-top: 2px; margin-bottom: 18px;
  }
  .contact-list { list-style: none; }
  .contact-item {
    display: flex; align-items: center; gap: 12px;
    font-size: 14px; color: var(--text-white);
    margin-bottom: 9px;
  }
  .contact-icon { width: 13px; height: 13px; fill: var(--text-white); flex: none; }
</style>
</head>
<body>
<main class="canvas">
  <section class="card card-front" aria-label="Card front">
    <span class="front-wordmark">Brightwave</span>
  </section>

  <section class="card card-back" aria-label="Card back">
    <header class="back-band">
      <span class="back-wordmark">Brightwave Renewables</span>
    </header>
    <div class="back-body">
      <h1 class="person-name">Daniel Hartwell</h1>
      <p class="person-role">Managing Director</p>
      <ul class="contact-list">
        <li class="contact-item">
          <svg class="contact-icon" viewBox="0 0 24 24"><path d="M6.6 10.8a15.1 15.1 0 0 0 6.6 6.6l2.2-2.2a1 1 0 0 1 1-.25 11.4 11.4 0 0 0 3.6.57 1 1 0 0 1 1 1V20a1 1 0 0 1-1 1A17 17 0 0 1 3 4a1 1 0 0 1 1-1h3.5a1 1 0 0 1 1 1c0 1.25.2 2.45.57 3.6a1 1 0 0 1-.25 1z"/></svg>
          +1 (555) 014-2278
        </li>
        <li class="contact-item">
          <svg class="contact-icon" viewBox="0 0 24 24"><path d="M12 2a10 10 0 1 0 0 20 10 10 0 0 0 0-20zm6.9 6h-2.9a15.6 15.6 0 0 0-1.4-3.6A8 8 0 0 1 18.9 8zM12 4a14 14 0 0 1 1.9 4h-3.8A14 14 0 0 1 12 4zM4.3 14a8 8 0 0 1 0-4h3.4a16.5 16.5 0 0 0 0 4zm.8 2h2.9a15.6 15.6 0 0 0 1.4 3.6A8 8 0 0 1 5.1 16zM8 8H5.1a8 8 0 0 1 4.3-3.6A15.6 15.6 0 0 0 8 8zm4 12a14 14 0 0 1-1.9-4h3.8A14 14 0 0 1 12 20zm2.3-6H9.7a14.7 14.7 0 0 1 0-4h4.6a14.7 14.7 0 0 1 0 4zm.3 5.6A15.6 15.6 0 0 0 16 16h2.9a8 8 0 0 1-4.3 3.6zM16.3 14a16.5 16.5 0 0 0 0-4h3.4a8 8 0 0 1 0 4z"/></svg>
          www.brightwave-renewables.com
        </li>
        <li class="contact-item">
          <svg class="contact-icon" viewBox="0 0 24 24"><path d="M2 5h20v14H2zm2 2v.5l8 5 8-5V7zm0 2.9V17h16V9.9l-8 5z"/></svg>
          daniel.hartwell@brightwave-renewables.com
        </li>
        <li class="contact-item">
          <svg class="contact-icon" viewBox="0 0 24 24"><path d="M12 2a7 7 0 0 0-7 7c0 5.2 7 13 7 13s7-7.8 7-13a7 7 0 0 0-7-7zm0 9.5A2.5 2.5 0 1 1 12 6.5a2.5 2.5 0 0 1 0 5z"/></svg>
          118 Meridian Lane, Portland, ME 04101
        </li>
      </ul>
    </div>
  </section>
</main>
</body>
</html>
```